Kestle company profile brochure

We are looking for a 2 - 4 page brochure for our company profile.
We’re Kestle, a team of town planning and traffic and transport engineering specialists located in Melbourne, Australia.
We would like a dynamic, exciting brochure that features the colours of our logo - blue, green and grey with orange as a feature colour.
The final result should convey that Kestle is:
-Reassuring and trustworthy
-Honest and direct
- Friendly and a bit kooky
-Laid-back and casual
-Fun to work with
-Highly knowledgeable within specific areas of expertise
-Polished and professional but not afraid to show a bit of personality
-Not as ‘hard edge’ as other planners or engineers
Kestle Consultants have created a business based on providing niche, expert advice across the two main areas of urban planning and traffic engineering as well as growing areas such as social and economic analysis. They are fiercely proud of the things that make them different to other firms – they take their responsibilities seriously, they are honest and up-front, they know how to work hard but also how to relax and have a laugh, and perhaps most importantly they know how to relate to people and they care about building successful relationships with their clients, colleagues and their staff. Kestle Consultants are united by our passion for shaping the city and their desire to ensure it develops sustainably.
Many similar businesses share some of these qualities, but Kestle is rare in that they deliver the whole package. This is evidenced by our ability to attract and retain high quality staff, by our long-standing client relationships and by their commitment to progressing our own company by commissioning a brochure and business card.

Target Market(s)

Kestle’s diverse client base consists of architecture practices, builders and developers, local government and the legal fraternity so these are the areas we market to.

Industry/Entity Type

Building

Requirements
Must have
• Must use our logos colours and logo.
The logo can be altered in that the type and image do not have stay exactly as it is on the JPEG - the words and image can be placed apart / together etc.
Nice to have
• We would like an image on the front cover that we can change
Page about disciplines

```html
<!DOCTYPE html>
<html lang="en">
<head>
<meta charset="utf-8">
<title>Kestle Company Profile Brochure</title>
<link href="https://fonts.googleapis.com/css2?family=Open+Sans:wght@300;400;600;700&display=swap" rel="stylesheet">
<style>
  :root {
    --backdrop: #e6e6e6;
    --paper: #ffffff;
    --ink: #3a3a3a;
    --ink-soft: #555555;
    --heading-grey: #5a5a5a;
    --brand-blue: #1e7bc4;
    --brand-green: #0f9a48;
    --tile-lime: #d4e27a;
    --tile-grey: #d5d6d8;
    --tile-peach: #fcd7b0;
    --tile-blue: #bedcf4;
    --tile-green: #c3e3b5;
  }
  * { box-sizing: border-box; margin: 0; padding: 0; }
  html, body { width: 1200px; height: 816px; overflow: hidden; }
  body {
    position: relative;
    background: var(--backdrop);
    font-family: "Open Sans", Arial, sans-serif;
    color: var(--ink);
  }
  .page {
    position: absolute;
    top: 85px;
    width: 519px;
    height: 670px;
    background: var(--paper);
    overflow: hidden;
    box-shadow: 0 2px 8px rgba(0,0,0,.25);
  }
  .page--inside { left: 49px; }
  .page--cover { left: 598px; }

  .tile { position: absolute; border-radius: 3px; }
  .tile--lime { background: var(--tile-lime); }
  .tile--grey { background: var(--tile-grey); }
  .tile--peach { background: var(--tile-peach); }
  .tile--blue { background: var(--tile-blue); }
  .tile--green { background: var(--tile-green); }

  .body-copy { position: absolute; font-size: 7.1px; line-height: 1.4; color: var(--ink-soft); }
  .body-copy p { margin-bottom: 7px; }

  .footer-band { position: absolute; left: 0; top: 0; width: 519px; height: 670px; }
  .footer-url {
    position: absolute; left: 44px; top: 603px;
    font-size: 23px; font-weight: 400; color: #fff; letter-spacing: .2px;
  }

  /* Inside page */
  .practice-areas { position: absolute; left: 236px; top: 25px; width: 260px; }
  .practice-areas__title { font-size: 8.6px; font-weight: 600; color: var(--brand-blue); margin-bottom: 8px; }
  .practice-areas__list { list-style: none; font-size: 7.1px; line-height: 11px; color: var(--ink-soft); }
  .practice-areas__list li { position: relative; padding-left: 13px; }
  .practice-areas__list li::before {
    content: ""; position: absolute; left: 0; top: 2px;
    width: 7px; height: 7px; border-radius: 50%;
    background: radial-gradient(circle at 35% 35%, #7fb6e6, var(--brand-blue));
  }
  .practice-areas__note { margin-top: 8px; font-size: 7.1px; line-height: 1.4; color: var(--ink-soft); }

  .team-photo {
    position: absolute; left: 236px; top: 191px; width: 252px; height: 144px;
    border-radius: 10px;
    background: linear-gradient(135deg, #cfd6dd 0%, #8e98a3 45%, #2f3338 100%);
  }
  .disciplines { position: absolute; left: 236px; top: 355px; width: 262px; }
  .disciplines__title { font-size: 18.5px; font-weight: 400; color: var(--heading-grey); letter-spacing: .3px; margin-bottom: 12px; }
  .disciplines__item h3 { font-size: 8px; font-weight: 600; color: var(--ink); margin-bottom: 5px; }
  .disciplines__item p { font-size: 7.1px; line-height: 1.4; color: var(--ink-soft); margin-bottom: 10px; }

  /* Cover page */
  .brand-name {
    position: absolute; left: 280px; top: 132px;
    font-size: 46px; font-weight: 400; color: #5b6066; letter-spacing: 1px; line-height: 1;
  }
  .cover-title { position: absolute; left: 35px; top: 158px; font-size: 21px; line-height: 1.1; font-weight: 400; letter-spacing: .3px; }
  .cover-title__top { display: block; color: var(--heading-grey); }
  .cover-title__bottom { display: block; color: var(--brand-blue); }
  .cover-photo {
    position: absolute; left: 35px; top: 233px; width: 484px; height: 352px;
    background: linear-gradient(90deg, rgba(255,255,255,1) 0%, rgba(255,255,255,0) 30%),
                linear-gradient(160deg, #eef1f4 0%, #c9b19c 35%, #b7c6d8 65%, #6f7d8d 100%);
  }
</style>
</head>
<body>

<section class="page page--inside" aria-label="Inside page">
  <div class="tile tile--lime" style="left:43px;top:0;width:46px;height:30px"></div>
  <div class="tile tile--lime" style="left:90px;top:0;width:46px;height:30px"></div>
  <div class="tile tile--grey" style="left:0;top:32px;width:42px;height:45px"></div>
  <div class="tile tile--peach" style="left:43px;top:32px;width:46px;height:45px"></div>
  <div class="tile tile--blue" style="left:43px;top:79px;width:46px;height:46px"></div>
  <div class="tile tile--green" style="left:90px;top:79px;width:46px;height:46px"></div>

  <div class="body-copy" style="left:35px;top:167px;width:162px">
    <p>Kestle has evaluated opportunities for developing and rehabilitating cities and regional areas. These studies are based upon an understanding of the natural features, environmental and visual constraints and opportunities.</p>
    <p>Demographic analysis, identifying tourist and employment potential and an analysis of existing services, can highlight the area's needs. These studies point the way for cities and regions, helping to maintain and enhance their physical and economic environments.</p>
    <p>Kestle has also been responsible for the evaluation and planning of individual large scale projects. Integrated project planning, where many different specialists within Kestle work together, offers our clients real benefits in terms of performance and the synthesis of ideas from many disciplines.</p>
    <p>Kestle also offers services from individual disciplines within the Company. Whether the service required is limited to a zoning assessment requiring Statutory Planners or site design, or requires only the expertise of Traffic Engineers, our professionals operate within a multi-disciplinary environment where feedback and advice from diverse specialists improve the end product for the benefit of our Clients.</p>
    <p>In all projects it is Kestle's aim to work closely with our clients to ensure that their priorities are met with quality advice and outputs.</p>
  </div>

  <div class="practice-areas">
    <h2 class="practice-areas__title">The principal areas of practice encompass:</h2>
    <ul class="practice-areas__list">
      <li>Integrated project planning</li>
      <li>Strategic planning</li>
      <li>Statutory planning</li>
      <li>Urban design</li>
      <li>Transportation planning</li>
      <li>Traffic and civil engineering</li>
      <li>Social and economic impact and analysis</li>
      <li>Demographic research</li>
    </ul>
    <p class="practice-areas__note">A client may require only one of the above services, either individually or to complete a project team. Alternatively Kestle may bring to a project many of the individual disciplines as an integrated team of people used to working closely together.</p>
  </div>

  <div class="team-photo" role="img" aria-label="Photo of a smiling team of five consultants gathered around a laptop"></div>

  <div class="disciplines">
    <h2 class="disciplines__title">DISCIPLINES</h2>
    <div class="disciplines__item">
      <h3>Planning</h3>
      <p>We use our extensive knowledge and experience to help our clients successfully navigate each step of the statutory and strategic planning processes.</p>
    </div>
    <div class="disciplines__item">
      <h3>Permit Applications</h3>
      <p>We have obtained planning permits for our clients on a variety of residential, commercial, entertainment and industrial projects in Melbourne, regional Victoria and interstate. Our consultative approach and extensive experience allows us to identify and resolve potential issues quickly.</p>
    </div>
    <div class="disciplines__item">
      <h3>SPT Advocacy</h3>
      <p>Due to our industry expertise, Kestle's planning team are regularly appointed as SPT advocates for private and public clients. We have acted as representatives for diverse project types at SPT appeals, mediations, planning panels and Consumer Affairs Office appeals.</p>
    </div>
  </div>

  <svg class="footer-band" viewBox="0 0 519 670" aria-hidden="true">
    <polygon points="0,569 519,601 519,605 0,573" fill="var(--brand-green)"/>
    <polygon points="0,579 519,611 519,636 0,659" fill="var(--brand-green)"/>
    <polygon points="0,664 519,641 519,645 0,668" fill="var(--brand-green)"/>
  </svg>
  <div class="footer-url">www.kestle.com.au</div>
</section>

<section class="page page--cover" aria-label="Cover page">
  <div class="tile tile--grey" style="left:0;top:0;width:52px;height:52px"></div>
  <div class="tile tile--peach" style="left:54px;top:0;width:52px;height:52px"></div>
  <div class="tile tile--blue" style="left:54px;top:54px;width:52px;height:52px"></div>
  <div class="tile tile--green" style="left:108px;top:54px;width:52px;height:52px"></div>

  <div class="brand-name">kestle</div>

  <h1 class="cover-title">
    <span class="cover-title__top">COMPANY</span>
    <span class="cover-title__bottom">PROFILE</span>
  </h1>

  <div class="cover-photo" role="img" aria-label="Photo of a smiling young professional woman at her desk, shown through a grid of rounded tiles"></div>

  <div class="body-copy" style="left:35px;top:233px;width:172px">
    <p>Kestle Consultants is a multi-disciplinary practice providing services in town and regional planning, transportation and civil engineering and urban design.</p>
    <p>Kestle has a fundamental commitment to the delivery of realistic and accurate advice to clients and progressive improvement of the environment through innovative planning and creative design solutions.</p>
    <p>There is a recognition today that new projects require sophisticated and detailed evaluation and planning so that the end result is complementary to the environment and that the physical and economic factors are understood before construction, or even before initial design work, is commenced.</p>
    <p>Kestle can offer a range of services at differing scales, providing a balanced perspective on a range of planning problems.</p>
  </div>

  <svg class="footer-band" viewBox="0 0 519 670" aria-hidden="true">
    <polygon points="0,569 519,601 519,605 0,573" fill="var(--paper)"/>
    <polygon points="0,575 519,607 519,610 0,578" fill="var(--brand-green)"/>
    <polygon points="0,579 519,611 519,636 0,659" fill="var(--brand-green)" stroke="var(--paper)" stroke-width="0"/>
    <polygon points="0,664 519,641 519,645 0,668" fill="var(--brand-green)"/>
  </svg>
  <div class="footer-url">www.kestle.com.au</div>
</section>

</body>
</html>
```